Business Card Design Project

Hello,

We have just created our new COMPANY LOGO via Fenwick Loom and would not like to turn our attention to new Business Cards.

We are a printing company based in Singapore & Las Vegas. We specialize in blue-print printing for the Architectural, Engineering and Construction industries

The design should be simple, professional, clean and organized.

The Business Cards should "pop" when seen and will hopefully be something that makes you look twice.

We have two different Pan-tones that we use for our company, feel free to use them if you think they will work for your design?

Orange: PMS 021
Gray: PMS 431

I have attached our current logo for your use and reference which should obvious be on our business cards.

Considering we have two locations on different continents, we need business cards templates where the address details need to be interchangeable for each different location (total 2)

First one:
42 Mereton Road #03-11 to #03-15
Singapore 512847
Tel : +65 6483-2207
Fax : +65 6487-9042

Second one:
3218 W. Larkspur Blvd, Suite 204
Las Vegas, Nevada 89147
Tel : (702) 555-0143
Fax : (702) 555-0178

We would also like to list a few of our key services on the card. Here are a few examples to get you going.

Plan Printing & Plotting
Digital Colour Printing
Cadline Printing
Specialty Book Making
Scanning & Archiving
Collection & Delivey

This is the first time i have requested for business cards to be created so please let me know if you require any additional information.
Many Thanks,
Tomas
Updates

Reason: It took us longer than expected to finalize our Company Logo We look forward to receiving your designs.

Target Market(s)

Our Target Market is construction related people.
Construction
Architecture
Engineering

Industry/Entity Type

Printing

Font styles to use
Other font styles liked:
• Times New Roman

Colors
faa54b
ffffff

Requirements
Must have
• The business card must have our Company Logo (attached)
The font used must be Times New Roman
Should not have
• Playful images of print designs and/or logos

```html
<!DOCTYPE html>
<html lang="en">
<head>
<meta charset="utf-8">
<title>Kestrel Print Works – Business Card</title>
<link rel="stylesheet" href="https://fonts.googleapis.com/css2?family=Tinos:ital,wght@0,400;0,700;1,700&display=swap">
<style>
  :root {
    --orange: #faa54b;
    --white: #ffffff;
    --ink: #000000;
    --edge: #a6a6a6;
    --stage-light: #ececec;
    --stage-dark: #c4c4c7;
  }
  * { margin: 0; padding: 0; box-sizing: border-box; }
  html, body {
    width: 1200px;
    height: 1000px;
    overflow: hidden;
  }
  body {
    position: relative;
    background: radial-gradient(ellipse at 50% 45%, var(--stage-light) 0%, var(--stage-dark) 85%);
    font-family: "Tinos", "Times New Roman", serif;
    color: var(--ink);
  }
  .card {
    position: absolute;
    left: 110px;
    top: 231px;
    width: 980px;
    height: 538px;
    border: 1px solid var(--edge);
    background: var(--white);
  }
  .card__header {
    position: absolute;
    left: 0; top: 0;
    width: 100%;
    height: 253px;
    background: var(--orange);
    text-align: center;
  }
  .brand-mark {
    position: absolute;
    left: 0; right: 0;
    top: 40px;
    font-size: 96px;
    font-weight: 700;
    line-height: 1;
    letter-spacing: -2px;
  }
  .brand-name {
    position: absolute;
    left: 0; right: 0;
    top: 150px;
    font-size: 36px;
    font-weight: 700;
    line-height: 1;
  }
  .brand-tagline {
    position: absolute;
    left: 0; right: 0;
    top: 196px;
    font-size: 25px;
    font-weight: 700;
    font-style: italic;
    line-height: 1;
  }
  .card__contact {
    position: absolute;
    left: 0; top: 253px;
    width: 100%;
    height: 173px;
    border-right: 1px solid var(--ink);
    text-align: center;
    font-size: 32px;
    line-height: 47px;
    padding-top: 12px;
  }
  .card__services {
    position: absolute;
    left: 0; bottom: 0;
    width: 100%;
    height: 112px;
    background: var(--orange);
    font-size: 25px;
    line-height: 1;
  }
  .service {
    position: absolute;
    white-space: nowrap;
    transform: translateX(-50%);
  }
  .row-1 { top: 25px; }
  .row-2 { top: 60px; }
</style>
</head>
<body>
  <section class="card">
    <header class="card__header">
      <div class="brand-mark">KPW</div>
      <div class="brand-name">Kestrel Print Works</div>
      <div class="brand-tagline">A Member of the KPW Group of Companies</div>
    </header>
    <address class="card__contact" style="font-style: normal;">
      <div>42 Mereton Road #03-11 to #03-15</div>
      <div>Singapore 512847</div>
      <div>Tel : +65 6483-2207, Fax : +65 6487-9042</div>
    </address>
    <footer class="card__services">
      <span class="service row-1" style="left:216px;">Plan Printing &amp; Plotting</span>
      <span class="service row-1" style="left:533px;">Digital Colour Printing</span>
      <span class="service row-1" style="left:819px;">Cadline Printing</span>
      <span class="service row-2" style="left:202px;">Specialty Book Making</span>
      <span class="service row-2" style="left:519px;">Scanning &amp; Archiving</span>
      <span class="service row-2" style="left:801px;">Collection &amp; Delivey</span>
    </footer>
  </section>
</body>
</html>
```